Restaurant needs a vertical banner for fried catfish

Our restaurant is looking for an eye-catching 78.75in. x 36in. vertical physical banner ad for our fried catfish. Photos for the fried catfish will be provided as a reference but we will also accept anything similar to the photo. We will be using the following as our receptacle: https://www.plorvista.com/banner-stand/retractable-banner-stands/
The design must incorporate the following flavor texts:
Fried Catfish
Always Fresh!
Made from Scratch
Hand-cut Fillets
The Best Catfish in Texas
Served with fries, hush puppies, and a 32oz fountain drink
Also available by the pound!
The final design should be creative, professional, and eye-catching for customers.
Updates
Need extra days to review
Colors
Designer to choose colors to be used in the design.
Requirements
Must have
- We are open to any and all design elements, albeit the 'flavor texts' should not overpower, but complement the fried catfish photo. 'Fried Catfish' can be used in lieu of a main title/logo.
Nice to have
- Transparent or textured backgrounds that can encompass any or all part of the banner such as a cutting board, shadows, abstract, etc to show depth are a plus.
- Use of vectors or objects such as ribbons or shapes to encapsulate the 'flavor texts' are also encouraged.

```html
<!DOCTYPE html>
<html lang="en">
<head>
<meta charset="utf-8">
<title>Fried Catfish – Vertical Banner</title>
<link href="https://fonts.googleapis.com/css2?family=EB+Garamond:ital,wght@0,500;1,500&family=Kaushan+Script&family=Open+Sans:wght@400&display=swap" rel="stylesheet">
<style>
  :root {
    --brown-dark: #3a2714;
    --brown-mid: #6b4a24;
    --brown-warm: #8c6431;
    --gold: #c89543;
    --cream: #f4e7c8;
    --charcoal: #1c1b1a;
    --charcoal-soft: #2b2926;
    --text-brown: #7a4f1c;
    --text-gold: #c8832e;
  }
  * { margin: 0; padding: 0; box-sizing: border-box; }
  html, body { width: 1200px; height: 2400px; overflow: hidden; background: #fff; }
  .banner { position: relative; width: 1200px; height: 2400px; overflow: hidden; }

  .stripes {
    position: absolute; left: 0; width: 100%;
    background: repeating-linear-gradient(180deg,
      var(--brown-dark) 0 22px, var(--brown-warm) 22px 44px,
      var(--gold) 44px 62px, var(--brown-mid) 62px 86px);
  }
  .stripes--top { top: 0; height: 255px; }
  .stripes--bottom { top: 2180px; height: 220px; }

  .title-band {
    position: absolute; top: 55px; left: 0; width: 100%; height: 150px;
    background: var(--brown-dark);
    display: flex; align-items: center; justify-content: center;
  }
  .title-band__name {
    font-family: "EB Garamond", serif; font-weight: 500; font-size: 112px;
    line-height: 1; color: var(--cream); letter-spacing: 2px;
  }

  .food-photo {
    position: absolute; top: 255px; left: 0; width: 100%; height: 860px;
    background:
      radial-gradient(ellipse at 60% 55%, #c9862f 0%, #a4651f 30%, transparent 60%),
      radial-gradient(ellipse at 25% 80%, #f1d27a 0%, #e2b656 35%, transparent 60%),
      linear-gradient(160deg, #6d3a1c 0%, #b87a36 45%, #efe2c4 100%);
  }

  .tagline {
    position: absolute; top: 440px; width: 100%; text-align: center;
    font-family: "Kaushan Script", cursive; font-size: 112px; line-height: 1.2; color: #fff;
    text-shadow: 0 4px 10px rgba(0,0,0,.55);
  }

  .divider { position: absolute; left: 0; width: 100%; height: 20px; background: var(--brown-dark); }
  .divider--photo { top: 1115px; }
  .divider--band { top: 1480px; height: 10px; background: var(--brown-mid); }

  .feature-panel {
    position: absolute; top: 1135px; left: 0; width: 100%; height: 345px;
    background: linear-gradient(180deg, #fff 0%, #f2efe9 100%);
    text-align: center; font-family: "EB Garamond", serif;
  }
  .feature-panel__main { margin-top: 130px; font-size: 104px; color: var(--text-brown); line-height: 1; }
  .feature-panel__sub { margin-top: 22px; font-size: 80px; color: var(--text-gold); line-height: 1; }

  .promise-band {
    position: absolute; top: 1490px; left: 0; width: 100%; height: 205px;
    background: linear-gradient(90deg, var(--brown-mid), var(--gold) 50%, var(--brown-mid));
    display: flex; align-items: center; justify-content: center;
  }
  .promise-band__text {
    font-family: "EB Garamond", serif; font-style: italic; font-size: 112px; color: var(--cream);
    text-shadow: 0 3px 6px rgba(0,0,0,.4); white-space: nowrap;
  }

  .offer-panel {
    position: absolute; top: 1700px; left: 0; width: 100%; height: 480px;
    background: linear-gradient(180deg, var(--charcoal-soft), var(--charcoal));
    text-align: center;
  }
  .offer-panel__details {
    margin-top: 125px; font-family: "EB Garamond", serif; font-size: 62px; line-height: 1.3;
    color: var(--text-gold); text-transform: uppercase;
  }
  .offer-panel__details small { font-size: 42px; text-transform: none; }
  .offer-panel__pound {
    position: absolute; bottom: 22px; width: 100%;
    font-family: "Open Sans", sans-serif; font-size: 66px; color: #fff; text-transform: uppercase;
  }
</style>
</head>
<body>
  <div class="banner">
    <div class="stripes stripes--top"></div>
    <header class="title-band"><h1 class="title-band__name">Fried Catfish</h1></header>
    <div class="food-photo" role="img" aria-label="Photo of golden fried catfish fillets on a plate with french fries, tomatoes and hush puppies"></div>
    <p class="tagline">Always Fresh!</p>
    <div class="divider divider--photo"></div>

    <section class="feature-panel">
      <p class="feature-panel__main">MADE FROM SCRATCH</p>
      <p class="feature-panel__sub">HAND-CUT FILLETS</p>
    </section>
    <div class="divider divider--band"></div>

    <section class="promise-band">
      <p class="promise-band__text">The Best Catfish in Texas</p>
    </section>

    <section class="offer-panel">
      <p class="offer-panel__details">Served with fries, hush puppies,<br>and a 32<small>oz</small> fountain drink</p>
      <p class="offer-panel__pound">Also available by the pound!</p>
    </section>

    <div class="stripes stripes--bottom"></div>
  </div>
</body>
</html>
```